We need a design for a Tequila line that will be infused with cannabis oil.
The design should have at least the following items.

The name Morvel Tequila
Marijuana leaf
200 ml fluid
500 mg THC

The lable to be printed will be clear "see through"
The liquid inside the clear bottle will be light gold in color.

Target Market(s)

Marijuana users

Requirements
Must have
• Marijuana leaf
• must say 200 ml
• must say 500 mg thc
Nice to have
• bottle lable will be clear on clear bottle.

```html
<!DOCTYPE html>
<html lang="en">
<head>
<meta charset="utf-8">
<title>Morvel Tequila – Label Line</title>
<link rel="stylesheet" href="https://fonts.googleapis.com/css2?family=Alfa+Slab+One&family=Marcellus&family=Lato:wght@700&display=swap">
<style>
  :root {
    --page: #f4f4f2;
    --frame: #111111;
    --frame-ornament: #3a3a3a;
    --clear-top: #eef4ee;
    --clear-bottom: #1e3b2b;
    --gold-top: #e6d548;
    --gold-bottom: #2c3a1c;
    --leaf: #3aa12f;
    --brand-red: #c8161d;
    --white: #ffffff;
    --ornament-clear: #3c5a48;
    --ornament-gold: #6b6a2a;
  }
  html, body {
    margin: 0;
    padding: 0;
    width: 1200px;
    height: 1200px;
    overflow: hidden;
    background: var(--page);
  }
  .canvas {
    position: relative;
    width: 1200px;
    height: 1200px;
  }
  .label {
    position: absolute;
    top: 320px;
    width: 460px;
    height: 559px;
  }
  .label--clear { left: 70px; }
  .label--gold { left: 670px; }
  .label__brand {
    font-family: "Alfa Slab One", serif;
    font-size: 52px;
    fill: var(--brand-red);
    letter-spacing: 1px;
  }
  .label__type {
    font-family: "Marcellus", serif;
    font-size: 30px;
    fill: var(--white);
    letter-spacing: 3px;
  }
  .label__detail {
    font-family: "Lato", sans-serif;
    font-weight: 700;
    font-size: 14px;
    fill: var(--white);
    letter-spacing: 1px;
  }
</style>
</head>
<body>
<main class="canvas">

  <svg class="label label--clear" viewBox="0 0 420 510" aria-label="Morvel Tequila label, clear edition">
    <rect class="label__frame" x="0" y="0" width="420" height="510" rx="22" fill="var(--frame)"/>
    <rect class="label__panel-top" x="40" y="40" width="340" height="220" fill="var(--clear-top)"/>
    <rect class="label__panel-bottom" x="40" y="260" width="340" height="210" fill="var(--clear-bottom)"/>
    <rect x="40" y="40" width="340" height="430" fill="none" stroke="var(--white)" stroke-width="2"/>
    <rect role="img" aria-label="Knotwork corner ornament" x="8" y="8" width="100" height="100" rx="14" fill="var(--frame-ornament)"/>
    <rect role="img" aria-label="Knotwork corner ornament" x="312" y="8" width="100" height="100" rx="14" fill="var(--frame-ornament)"/>
    <rect role="img" aria-label="Knotwork corner ornament" x="8" y="402" width="100" height="100" rx="14" fill="var(--frame-ornament)"/>
    <rect role="img" aria-label="Knotwork corner ornament" x="312" y="402" width="100" height="100" rx="14" fill="var(--frame-ornament)"/>
    <ellipse role="img" aria-label="Cannabis leaf illustration" cx="210" cy="100" rx="55" ry="40" fill="var(--leaf)"/>
    <text class="label__brand" x="210" y="205" text-anchor="middle">MORVEL</text>
    <rect class="label__banner" x="100" y="225" width="220" height="48" fill="var(--brand-red)" stroke="var(--white)" stroke-width="3"/>
    <text class="label__type" x="210" y="259" text-anchor="middle">TEQUILA</text>
    <rect role="img" aria-label="Scroll ornament" x="140" y="290" width="140" height="30" rx="12" fill="var(--ornament-clear)"/>
    <rect class="label__ribbon" x="145" y="330" width="130" height="28" rx="4" fill="var(--frame)" stroke="var(--white)" stroke-width="2"/>
    <text class="label__detail" x="210" y="349" text-anchor="middle">500 MG THC</text>
    <line x1="170" y1="400" x2="250" y2="400" stroke="var(--white)" stroke-width="1.5"/>
    <text class="label__detail" x="210" y="422" text-anchor="middle">200 ML</text>
  </svg>

  <svg class="label label--gold" viewBox="0 0 420 510" aria-label="Morvel Tequila label, gold edition">
    <rect class="label__frame" x="0" y="0" width="420" height="510" rx="22" fill="var(--frame)"/>
    <rect class="label__panel-top" x="40" y="40" width="340" height="220" fill="var(--gold-top)"/>
    <rect class="label__panel-bottom" x="40" y="260" width="340" height="210" fill="var(--gold-bottom)"/>
    <rect x="40" y="40" width="340" height="430" fill="none" stroke="var(--gold-top)" stroke-width="2"/>
    <rect role="img" aria-label="Knotwork corner ornament" x="8" y="8" width="100" height="100" rx="14" fill="var(--ornament-gold)"/>
    <rect role="img" aria-label="Knotwork corner ornament" x="312" y="8" width="100" height="100" rx="14" fill="var(--ornament-gold)"/>
    <rect role="img" aria-label="Knotwork corner ornament" x="8" y="402" width="100" height="100" rx="14" fill="var(--ornament-gold)"/>
    <rect role="img" aria-label="Knotwork corner ornament" x="312" y="402" width="100" height="100" rx="14" fill="var(--ornament-gold)"/>
    <ellipse role="img" aria-label="Cannabis leaf illustration" cx="210" cy="100" rx="55" ry="40" fill="var(--leaf)"/>
    <text class="label__brand" x="210" y="205" text-anchor="middle">MORVEL</text>
    <rect class="label__banner" x="100" y="225" width="220" height="48" fill="var(--brand-red)" stroke="var(--gold-top)" stroke-width="3"/>
    <text class="label__type" x="210" y="259" text-anchor="middle" style="fill: var(--gold-top)">TEQUILA</text>
    <rect role="img" aria-label="Scroll ornament" x="140" y="290" width="140" height="30" rx="12" fill="var(--ornament-gold)"/>
    <rect class="label__ribbon" x="145" y="330" width="130" height="28" rx="4" fill="var(--frame)" stroke="var(--gold-top)" stroke-width="2"/>
    <text class="label__detail" x="210" y="349" text-anchor="middle" style="fill: var(--gold-top)">500 MG THC</text>
    <line x1="170" y1="400" x2="250" y2="400" stroke="var(--gold-top)" stroke-width="1.5"/>
    <text class="label__detail" x="210" y="422" text-anchor="middle" style="fill: var(--gold-top)">200 ML</text>
  </svg>

</main>
</body>
</html>
```